Website for a building supplies and prefabricated timber wall and roof manafacturer.

Develop a brand new website for a building supply business providing a number of services and products to Brickmere Supply Co. Logo will be supplied. A website I like and a competitor is https://www.tarlowbuild.com.au/ also attached are some other screen dumps of ones I like.

Our parent company is ferncastholdings.com.au but this webapge is being developed as we are breaking away from the parent body.
Updates

Re Garantee: The business does not currently have a website, so it is highly probable that we will achieve an outcome for this competition but I cant garantee it as I am not sure what the quality of submissions will be. I have recently run another competition for another business on another forum and paid out on that. Platform: I dont mind what platform the website is built on, however i understood this to be a Wordpress site. Other: I cant read the comments from the portal, I will post reponses here. Thanks ... Niv

Target Market(s)

Brickmere Supply Co in Melbourne Australia

Industry/Entity Type

Building Product

Coding

Coded - Design and coding required

Font styles to use
Sans Serif

Colors
ec1f27
ffffff
000000

Requirements
Must have
• Start with smartphone functionality as I feel more people will viewit first on smart phones.
• Primary admin access.
• Ability to be able to edit, add photos and pages ourselves.
Nice to have
• I like the rolling banner across the top and then the tiles below with our products and services.
• i like https://www.tarlowbuild.com.au/ and attached are some screen dumps of othersites i like.

```html
<!DOCTYPE html>
<html lang="en">
<head>
<meta charset="utf-8">
<title>Brickmere Supply — One Shop For All Your Building Needs</title>
<link href="https://fonts.googleapis.com/css2?family=Poppins:wght@300;400;500;600;700;800&family=Roboto:wght@300;400&family=Oswald:wght@400;500&display=swap" rel="stylesheet">
<style>
:root{
  --red:#ec1f27;
  --red-dark:#a8141a;
  --white:#ffffff;
  --black:#000000;
  --ink:#333333;
  --muted:#777777;
  --line:#e3e3e3;
  --footer-dark:#2b2b2b;
}
*{box-sizing:border-box;margin:0;padding:0}
html,body{width:1200px;height:2757px;overflow:hidden;background:var(--white)}
body{font-family:"Poppins",sans-serif;color:var(--ink);position:relative}
.abs{position:absolute}

/* top bar */
.topbar{top:0;left:0;width:1200px;height:26px;border-bottom:1px solid var(--line);font-size:9px;font-weight:600}
.topbar .call{left:235px;top:7px;color:var(--ink)}
.topbar .util{left:828px;top:6px;display:flex;gap:8px;align-items:center;font-weight:400}
.topbar svg{width:10px;height:10px}

/* header */
.header{top:26px;left:0;width:1200px;height:60px}
.brand{left:233px;top:8px;display:flex;align-items:center;gap:6px}
.brand-square{width:20px;height:20px;background:var(--red)}
.brand-name{font-weight:800;font-size:20px;color:var(--red);letter-spacing:.5px}
.mainnav{right:233px;top:20px;display:flex;gap:12px}
.mainnav a{font-size:9px;font-weight:600;color:var(--ink);text-decoration:none;padding:2px 4px 5px;border-bottom:2px solid var(--ink)}

/* category bar */
.catbar{top:86px;left:0;width:1200px;height:37px;background:linear-gradient(90deg,#2e6da4 0%,#355f8f 45%,#8e1d28 60%,#8b1219 100%);display:flex;justify-content:center;gap:46px;align-items:center}
.catbar a{color:var(--white);font-size:9px;font-weight:600;text-decoration:none}

/* hero */
.hero-photo{top:123px;left:0;width:640px;height:423px;background:linear-gradient(180deg,#4a8fd6 0%,#8dbbe8 40%,#9c8a74 62%,#6f9a3c 78%,#cfcbc2 100%)}
.hero-panel{top:123px;left:640px;width:560px;height:423px;background:var(--red);color:var(--white)}
.hero-inner{position:absolute;left:0;top:100px;width:320px;text-align:center}
.hero-title{font-family:"Oswald",sans-serif;font-weight:400;font-size:40px;line-height:48px;letter-spacing:3px;color:transparent;-webkit-text-stroke:1.2px var(--white)}
.hero-rule{width:286px;height:3px;background:var(--white);margin:2px auto 10px}
.hero-sub{font-family:"Roboto",sans-serif;font-weight:300;font-size:27px;line-height:34px}
.btn-outline{display:inline-block;margin-top:30px;width:162px;height:50px;line-height:46px;border:2px solid var(--white);font-size:13px;font-weight:600;letter-spacing:1.5px;color:var(--white)}
.slider-arrows{top:492px;left:556px}

/* intro */
.intro-rule{top:624px;left:245px;width:287px;height:2px;background:var(--red)}
.intro-rule::after{content:"";position:absolute;left:115px;top:-2px;width:60px;height:6px;background:var(--red)}
.intro-heading{top:646px;left:245px;font-size:33px;font-weight:800;line-height:38px;letter-spacing:4px;color:var(--red)}
.intro-title{top:596px;left:629px;font-size:19px;font-weight:700;letter-spacing:2px;line-height:22px;color:var(--ink)}
.intro-copy{top:662px;left:629px;width:300px;font-size:9px;line-height:15px;letter-spacing:.8px;color:var(--muted)}
.btn-red{top:762px;left:629px;width:108px;height:32px;background:var(--red);color:var(--white);font-size:10px;font-weight:600;letter-spacing:1.5px;text-align:center;line-height:28px;border:2px solid #c0151c}

/* section titles */
.house-icon{width:48px;height:46px;left:576px}
.section-title{left:0;width:1200px;text-align:center;font-family:"Oswald",sans-serif;font-weight:400;font-size:30px;letter-spacing:7px;color:transparent;-webkit-text-stroke:1px #8a8a8a}
.section-sub{top:950px;left:0;width:1200px;text-align:center;font-size:10px;letter-spacing:.6px;color:var(--muted)}

/* category tiles */
.tile{top:983px;width:223px;height:267px}
.tile.kitchen{left:246px;background:linear-gradient(160deg,#c9c9c7 0%,#8d8a86 45%,#9b7a55 70%,#4e4c4a 100%)}
.tile.bath{left:491px;background:linear-gradient(170deg,#e8d8d6 0%,#d6c2c0 60%,#c4b1ae 100%)}
.tile.laundry{left:731px;background:linear-gradient(170deg,#c9a56c 0%,#e6e3de 35%,#d9d7d3 70%,#8f8b86 100%)}
.tile-caption{position:absolute;left:0;bottom:0;width:100%;height:58px;background:var(--red);color:var(--white);padding:12px 10px}
.tile-caption b{display:block;font-size:13px;font-weight:600;letter-spacing:1.5px;line-height:18px}
.tile-caption span{font-size:10px;letter-spacing:1px}
.dots{top:1273px;left:550px;display:flex;gap:12px}
.dots i{display:block;width:26px;height:4px;background:#9a9a9a}
.dots i:first-child{background:var(--red)}

/* features */
.features{top:1342px;left:0;width:1200px;height:263px;background:linear-gradient(180deg,#5b5446 0%,#6e6453 45%,#4c4438 100%)}
.feature{top:1388px;width:168px;height:168px;border-radius:50%;background:var(--white);border:7px solid var(--red);text-align:center}
.feature svg{margin-top:24px;width:58px;height:58px}
.feature p{font-size:11px;letter-spacing:.8px;line-height:14px;color:var(--ink);margin-top:6px;white-space:nowrap}

/* products */
.prod-arrows{top:1757px;left:918px}
.product{top:1779px;width:147px;height:219px;border:1px solid var(--line)}
.product .img{height:148px}
.product .name{font-size:9px;letter-spacing:.6px;line-height:15px;color:var(--muted);padding:6px 4px 0}
.product .price{position:absolute;left:4px;bottom:8px;font-size:9px;color:var(--muted)}
.product .cart{position:absolute;right:4px;bottom:6px;width:16px;height:16px;border-radius:50%;background:var(--red)}

/* promos */
.promo{top:2035px;width:337px;height:213px;color:var(--white)}
.promo.heat{left:246px;background:linear-gradient(160deg,#7b7b79 0%,#555452 55%,#3f3e3c 100%)}
.promo.small{left:618px;background:linear-gradient(160deg,#9a9a98 0%,#6d6c6a 55%,#4b4a48 100%)}
.promo .deal{position:absolute;left:0;width:100%;top:64px;text-align:center;font-size:30px;font-weight:400}
.promo .deal b{font-size:64px;font-weight:700;color:#f7c21b;letter-spacing:-1px}
.promo .pct{display:inline-block;width:32px;height:32px;border-radius:50%;background:var(--red);color:var(--white);font-size:20px;font-weight:700;line-height:32px;vertical-align:28px;margin-left:-14px}
.promo .label{position:absolute;left:0;width:100%;top:138px;text-align:center;font-size:14px;font-weight:600;letter-spacing:1.5px}

/* brands */
.brands-title{top:2277px;left:0;width:1200px;text-align:center;font-family:"Oswald",sans-serif;font-weight:400;font-size:19px;letter-spacing:3px;color:transparent;-webkit-text-stroke:.8px #8a8a8a}
.brand-row{top:2336px;display:flex;justify-content:space-between;align-items:center}
.brand-row span{font-size:21px;font-weight:700}
.b1,.b4{color:var(--red)}.b2{color:#1f5fa8}.b3{color:#1f7fc4}.b5{color:var(--black)}

/* footer */
.footer{top:2395px;left:0;width:1200px;height:274px;background:var(--red);color:var(--white)}
.fcol{top:40px;width:150px}
.fcol h4{font-size:10px;font-weight:600;padding-bottom:6px;border-bottom:2px solid var(--white);margin-bottom:10px}
.fcol li{list-style:none;font-size:9px;font-weight:600;line-height:15px}
.fcol li::before{content:"→ ";font-weight:400}
.contact-row{display:flex;gap:10px;align-items:center;font-size:9px;line-height:14px;margin-bottom:18px}
.contact-row i{flex:none;width:18px;height:18px;border-radius:50%;background:var(--white)}
.about{font-size:9px;line-height:15px}
.follow{font-size:10px;margin:4px 0 8px}
.socials{display:flex;gap:11px}
.socials i{width:18px;height:18px;border:1.5px solid var(--white)}
.paycards{display:flex;gap:6px}
.paycards span{background:var(--white);color:var(--ink);font-size:8px;font-weight:600;padding:3px 6px}
.copyright{top:2669px;left:0;width:1200px;height:88px;background:var(--footer-dark);color:#dddddd;font-size:10px;text-align:center;line-height:88px}
</style>
</head>
<body>

<div class="abs topbar">
  <span class="abs call">Order online or call us (1800) 555 0142</span>
  <div class="abs util">
    <svg viewBox="0 0 10 10"><circle cx="4" cy="4" r="3" fill="none" stroke="#333" stroke-width="1.3"/><path d="M6 6l3 3" stroke="#333" stroke-width="1.3"/></svg>|
    <svg viewBox="0 0 10 10"><circle cx="5" cy="3" r="2.2" fill="#333"/><path d="M1 10c0-3 8-3 8 0z" fill="#333"/></svg>|
    <svg viewBox="0 0 10 10"><path d="M5 9L1 5a2.2 2.2 0 014-3 2.2 2.2 0 014 3z" fill="#333"/></svg>|
    <svg viewBox="0 0 10 10"><path d="M0 1h2l1.5 5h5l1-3.5H3" fill="none" stroke="#333"/><circle cx="4" cy="8.5" r="1" fill="#333"/><circle cx="8" cy="8.5" r="1" fill="#333"/></svg>
    <span>My Cart: 0 Item</span>
  </div>
</div>

<header class="abs header">
  <div class="abs brand"><span class="brand-square"></span><span class="brand-name">BRICKMERE SUPPLY</span></div>
  <nav class="abs mainnav"><a>Catalogue</a><a>Cooking Demos</a><a>Blog</a><a>About Us</a><a>Contact Us</a></nav>
</header>

<nav class="abs catbar">
  <a>Kitchen &amp; Cooking</a><a>Bathroom</a><a>Alfresco</a><a>Heating &amp; Cooling</a><a>Small Appliances</a><a>Promotions</a>
</nav>

<div class="abs hero-photo" role="img" aria-label="Large brick family home with a curved driveway and green lawn under a blue sky"></div>
<section class="abs hero-panel">
  <div class="hero-inner">
    <h1 class="hero-title">ONE SHOP</h1>
    <div class="hero-rule"></div>
    <p class="hero-sub">For All Your<br>Building Needs</p>
    <a class="btn-outline">BUY NOW</a>
  </div>
</section>
<svg class="abs slider-arrows" width="60" height="30" viewBox="0 0 60 30"><path d="M22 3L10 15l12 12" fill="none" stroke="#555" stroke-width="6"/><path d="M38 3l12 12-12 12" fill="none" stroke="#555" stroke-width="6"/></svg>

<div class="abs intro-rule"></div>
<h2 class="abs intro-heading">HIGH QUALITY<br>CONSTRUCTION<br>MATERIALS</h2>
<h3 class="abs intro-title">Find Top Construction<br>Products in the Industry</h3>
<p class="abs intro-copy">Obvious that the better your future house will be, the better new life you will get. To achieve this, the first thing you should think of is building materials. Our store offers all needed ingredients to make you new house - new life - beautiful, high quality and original.</p>
<a class="abs btn-red">READ MORE</a>

<svg class="abs house-icon" style="top:838px" viewBox="0 0 48 46"><path d="M4 22L24 4l20 18" fill="none" stroke="#ec1f27" stroke-width="2.5"/><path d="M10 18v26h28V18" fill="none" stroke="#ec1f27" stroke-width="2.5"/><rect x="19" y="28" width="10" height="16" fill="none" stroke="#ec1f27" stroke-width="2.5"/></svg>
<h2 class="abs section-title" style="top:900px">PRODUTS CATEGORY</h2>
<p class="abs section-sub">Obvious that the better your future house will be, the better new life you will get.</p>

<div class="abs tile kitchen" role="img" aria-label="Modern kitchen with timber island bench and range hood"></div>
<div class="abs tile bath" role="img" aria-label="Pale pink tiled bathroom with basin and toilet">
  <div class="tile-caption"><b>Kitchen &amp; Cooking</b><span>View all...</span></div>
</div>
<div class="abs tile laundry" role="img" aria-label="Laundry room with front-loading washer and dryer"></div>
<div class="abs dots"><i></i><i></i><i></i></div>

<section class="abs features" role="img" aria-label="Dim bathroom vanity with brass taps and plants in the background"></section>
<div class="abs feature" style="left:274px">
  <svg viewBox="0 0 60 60"><circle cx="30" cy="30" r="28" fill="none" stroke="#ec1f27" stroke-width="2"/><rect x="13" y="22" width="20" height="15" fill="#333"/><path d="M33 26h8l5 6v5H33z" fill="#333"/><circle cx="20" cy="39" r="3" fill="#333"/><circle cx="40" cy="39" r="3" fill="#333"/></svg>
  <p>100% Free Delivery<br>OVER $59</p>
</div>
<div class="abs feature" style="left:517px">
  <svg viewBox="0 0 60 60"><circle cx="30" cy="30" r="28" fill="none" stroke="#ec1f27" stroke-width="2"/><rect x="17" y="21" width="26" height="20" rx="3" fill="none" stroke="#333" stroke-width="2.5"/><path d="M20 21l14-5 3 5" fill="none" stroke="#333" stroke-width="2"/><circle cx="37" cy="31" r="2" fill="#333"/></svg>
  <p>100% Back to money<br>ALL ORDERS</p>
</div>
<div class="abs feature" style="left:761px">
  <svg viewBox="0 0 60 60"><circle cx="30" cy="30" r="28" fill="none" stroke="#ec1f27" stroke-width="2"/><path d="M18 20c0 12 10 22 22 22l3-5-6-3-3 3c-4-2-8-6-10-10l3-3-3-6z" fill="#333"/><circle cx="38" cy="22" r="6" fill="#333"/></svg>
  <p>Support Customer<br>SUPPORT 24/7</p>
</div>

<svg class="abs house-icon" style="top:1643px" viewBox="0 0 48 46"><path d="M4 22L24 4l20 18" fill="none" stroke="#ec1f27" stroke-width="2.5"/><path d="M10 18v26h28V18" fill="none" stroke="#ec1f27" stroke-width="2.5"/><rect x="19" y="28" width="10" height="16" fill="none" stroke="#ec1f27" stroke-width="2.5"/></svg>
<h2 class="abs section-title" style="top:1704px">OUR PRODUTS</h2>
<svg class="abs prod-arrows" width="34" height="14" viewBox="0 0 34 14"><path d="M13 7H2M6 3L2 7l4 4" fill="none" stroke="#333" stroke-width="1.8"/><path d="M21 7h11M28 3l4 4-4 4" fill="none" stroke="#333" stroke-width="1.8"/></svg>

<div class="abs product" style="left:246px"><div class="img" role="img" aria-label="Chrome mixer tap over a white basin" style="background:linear-gradient(160deg,#7a7a7a,#e9e9e9 55%,#cfcfcf)"></div><p class="name">Cherry Wood Dark Walnut<br>Early American Golden</p><span class="price">$10.00–$20.00</span><i class="cart"></i></div>
<div class="abs product" style="left:432px"><div class="img" role="img" aria-label="Round white basin set in a stone benchtop" style="background:linear-gradient(160deg,#8d7c68,#ece8e2 55%,#a59482)"></div><p class="name">Cherry Wood Dark Walnut<br>Early American Golden</p><span class="price">$10.00–$20.00</span><i class="cart"></i></div>
<div class="abs product" style="left:618px"><div class="img" role="img" aria-label="White wall-mounted heating unit" style="background:linear-gradient(180deg,#f1f1f1,#dcdcdc 60%,#c9c9c9)"></div><p class="name">Cherry Wood Dark Walnut<br>Early American Golden</p><span class="price">$10.00–$20.00</span><i class="cart"></i></div>
<div class="abs product" style="left:803px"><div class="img" role="img" aria-label="Stainless steel built-in microwave oven" style="background:linear-gradient(180deg,#dedede,#7d7d7d 55%,#c9c9c9)"></div><p class="name">Cherry Wood Dark Walnut<br>Early American Golden</p><span class="price">$10.00–$20.00</span><i class="cart"></i></div>

<div class="abs promo heat" role="img" aria-label="Kitchen with built-in ovens">
  <p class="deal">up to <b>60</b><span class="pct">%</span>OFF</p>
  <p class="label">Heating &amp; Cooling</p>
</div>
<div class="abs promo small" role="img" aria-label="Bright modern bathroom">
  <p class="deal">up to <b>20</b><span class="pct">%</span>OFF</p>
  <p class="label">Small Appliances</p>
</div>

<h2 class="abs brands-title">Brands We Work With</h2>
<svg class="abs" style="top:2342px;left:246px" width="14" height="24" viewBox="0 0 14 24"><path d="M12 2L2 12l10 10" fill="none" stroke="#111" stroke-width="3"/></svg>
<div class="abs brand-row" style="left:288px;width:624px">
  <span class="b1">Torvane</span><span class="b2">Corbel</span><span class="b3">Lumenly</span><span class="b4">Halden</span><span class="b5">Ostler Tools</span>
</div>
<svg class="abs" style="top:2342px;left:940px" width="14" height="24" viewBox="0 0 14 24"><path d="M2 2l10 10L2 22" fill="none" stroke="#111" stroke-width="3"/></svg>

<footer class="abs footer">
  <div class="abs fcol" style="left:246px">
    <h4>Contact Us</h4>
    <div class="contact-row"><i></i><span>48 Quarry Lane, Dandenong South,<br>Melbourne Australia</span></div>
    <div class="contact-row"><i></i><span>+61 (0) 3 9555 0117</span></div>
    <div class="contact-row"><i></i><span>sales@brickmeresupply.example</span></div>
    <p class="follow">Follow us</p>
    <div class="socials"><i></i><i></i><i></i><i></i><i></i></div>
  </div>
  <div class="abs fcol" style="left:430px">
    <h4>Category</h4>
    <ul><li>Kitchen &amp; Cooking</li><li>Bathroom</li><li>Alfresco</li><li>Small Appliances</li><li>Promotions</li><li>Laundry</li></ul>
  </div>
  <div class="abs fcol" style="left:619px">
    <h4>My Account</h4>
    <ul><li>My Account</li><li>Log in</li><li>My Addresses</li><li>My Orders</li><li>Wishlist</li><li>Delivery Information</li></ul>
  </div>
  <div class="abs fcol" style="left:801px">
    <h4>About</h4>
    <p class="about">Lorem Ipsum is simply dummy text of the printing and typesetting industry. Lorem Ipsum has been the industry's standard dummy text ever since the 1500s, when an unknown printer took a galley of type and scrambled it to</p>
    <p class="about" style="text-align:right;margin-top:6px">Read More</p>
    <p class="follow" style="margin-top:10px">Pay us</p>
    <div class="paycards"><span>Cardline</span><span>Paywell</span></div>
  </div>
</footer>
<div class="abs copyright">© Copyright 2019 Brickmere Supply Co . All Rights Reserved</div>

</body>
</html>
```